Design for Chirpwall Ad to promote Laptops purchase

Need a graphic design for a Chirpwall Ad - to promote 2 laptops (PC and Zorvane) with the stated required ad-text.

AD TEXT:

FOR SME BUSINESS ONLY!
Chat with us!
To get advice on how to apply
and defray up to 80%* of business laptop purchase cost!

*Terms and Conditions apply

Image for reference only

Target Market(s)

Small medium business

Font styles to use
Sans Serif

Requirements
Must have
• 2 laptop images (see attached ) - 1 vector image of ZORVANE , and pls try to create another vector image of PC laptop (where screen is showing Blue Pendrel screen)

```html
<!DOCTYPE html>
<html lang="en">
<head>
<meta charset="utf-8">
<title>Chirpwall Ad – SME Business Laptops</title>
<link rel="stylesheet" href="https://fonts.googleapis.com/css2?family=Montserrat:wght@400;500;700;800&display=swap">
<style>
  :root {
    --backdrop: #d6d6d6;
    --brand-deep: #1d6ac0;
    --brand-sky: #4fa8f4;
    --paper: #ffffff;
    --heading-blue: #1b63b1;
    --ink: #2f2f2f;
    --ink-soft: #3a3a3a;
    --note-ink: #10243d;
  }
  * { box-sizing: border-box; margin: 0; padding: 0; }
  html, body {
    width: 1129px;
    height: 1200px;
    overflow: hidden;
    background: var(--backdrop);
    font-family: "Montserrat", Arial, sans-serif;
  }
  .ad-card {
    position: absolute;
    left: 89px;
    top: 101px;
    width: 951px;
    height: 951px;
    overflow: hidden;
    background: var(--paper);
    box-shadow: 8px 10px 14px rgba(0, 0, 0, 0.28);
  }
  .ad-backdrop {
    position: absolute;
    inset: 0;
    width: 100%;
    height: 100%;
  }
  .ad-headline {
    position: absolute;
    left: 0;
    right: 0;
    top: 62px;
    text-align: center;
    color: var(--paper);
    font-size: 53px;
    font-weight: 400;
    line-height: 62px;
    letter-spacing: 0.5px;
    white-space: nowrap;
  }
  .ad-headline strong { font-weight: 700; }
  .reference-note {
    position: absolute;
    left: 30px;
    top: 366px;
    transform: translate(-50%, -50%) rotate(-90deg);
    white-space: nowrap;
    font-size: 13px;
    color: var(--note-ink);
  }
  .product-photo {
    position: absolute;
    border-radius: 18px;
    box-shadow: 0 14px 22px rgba(8, 30, 60, 0.35);
  }
  .product-photo--zorvane {
    left: 95px;
    top: 172px;
    width: 464px;
    height: 321px;
    background:
      radial-gradient(ellipse 60% 55% at 50% 40%, #e6a6e8 0%, rgba(230, 166, 232, 0) 70%),
      linear-gradient(180deg, #8d3fae 0%, #b65fc4 45%, #5a2a84 78%, #b8b8bc 92%, #8e8e92 100%);
  }
  .product-photo--pendrel {
    left: 353px;
    top: 313px;
    width: 527px;
    height: 338px;
    background:
      radial-gradient(ellipse 45% 40% at 65% 35%, #6fd0f5 0%, rgba(111, 208, 245, 0) 70%),
      linear-gradient(180deg, #0c3a6a 0%, #1273b5 40%, #0a2f5a 68%, #bdb6a8 80%, #8f897d 100%);
  }
  .ad-cta {
    position: absolute;
    left: 0;
    right: 0;
    top: 722px;
    text-align: center;
    color: var(--heading-blue);
    font-size: 54px;
    font-weight: 800;
    line-height: 62px;
  }
  .ad-body {
    position: absolute;
    left: 0;
    right: 0;
    top: 796px;
    text-align: center;
    color: var(--ink);
    font-size: 28px;
    font-weight: 500;
    line-height: 37px;
    white-space: nowrap;
  }
  .ad-terms {
    position: absolute;
    right: 59px;
    top: 899px;
    color: var(--ink-soft);
    font-size: 19px;
    font-weight: 400;
  }
</style>
</head>
<body>
  <main class="ad-card">
    <svg class="ad-backdrop" viewBox="0 0 800 800" preserveAspectRatio="none">
      <defs>
        <linearGradient id="cityTint" x1="0" y1="0" x2="1" y2="1">
          <stop offset="0" stop-color="#2a78c8"/>
          <stop offset="0.5" stop-color="#1d6ac0"/>
          <stop offset="1" stop-color="#1a5fae"/>
        </linearGradient>
      </defs>
      <rect class="city-photo" x="0" y="0" width="800" height="600" fill="url(#cityTint)" role="img" aria-label="Blue-tinted photo of office towers seen from below"/>
      <polygon class="sky-band" points="0,440 575,522 0,572" fill="var(--brand-sky)"/>
      <polygon class="paper-panel" points="0,572 800,540 800,800 0,800" fill="var(--paper)"/>
    </svg>

    <h1 class="ad-headline">FOR <strong>SME BUSINESS</strong> ONLY!</h1>

    <p class="reference-note">Images for reference only</p>

    <div class="product-photo product-photo--zorvane" role="img" aria-label="Photo of a silver Zorvane laptop with a purple galaxy screen"></div>
    <div class="product-photo product-photo--pendrel" role="img" aria-label="Photo of a PC laptop showing a blue Pendrel desktop screen"></div>

    <h2 class="ad-cta">Chat with us!</h2>
    <p class="ad-body">To get advice on how to apply and<br>defray upto 80% of business laptop purchase cost!</p>
    <p class="ad-terms">*Terms &amp; Conditions apply</p>
  </main>
</body>
</html>
```